Book cover design for modern bagpipe music book

This music book will be A4 in size and requires a design for the front and back cover. The focus is on creating a modern and eye catching design, breaking away from the stereotypes of what people think of when they think of bagpipes. Think the OPPOSITE of a bagpiper in a full kilt standing on top of a mountain playing Copper Lanterns Rising!

Book title: Rise Hum March Rest

Other front cover text : Music for the bagpipes by Dermot Fairley

Front cover file ideas uploaded

2 pictures of bagpipes attached.

- The real set of bagpipes give an idea of the correct finer details

- The toy bagpipes perhaps have a better shape with the left 'stick' down

Back cover - No real brief. Keen for it not to be a full block single colour though.

Design requires 3mm bleed for print

Open to ideas and suggestions! Thank you!

```html
<!DOCTYPE html>
<html lang="en">
<head>
<meta charset="utf-8">
<title>Rise Hum March Rest – Cover</title>
<link href="https://fonts.googleapis.com/css2?family=Red+Hat+Display:wght@500;600;700&display=swap" rel="stylesheet">
<style>
  :root {
    --page: #f1f1f1;
    --cover-green: #a9d174;
    --title-red: #f20c0c;
    --ink: #111111;
    --art-dark: #2a2f22;
    --art-mid: #6f7d58;
  }
  * { margin: 0; padding: 0; box-sizing: border-box; }
  html, body {
    width: 1200px; height: 800px; overflow: hidden;
    background: var(--page);
  }
  .stage {
    position: relative; width: 1200px; height: 800px;
  }
  .cover {
    position: absolute; left: 346px; top: 40px;
    width: 509px; height: 720px;
    background: var(--cover-green);
    font-family: "Red Hat Display", "Helvetica Neue", Arial, sans-serif;
    overflow: hidden;
  }
  .hero-art {
    position: absolute; left: 120px; top: 45px;
    width: 300px; height: 200px;
    border-radius: 0 60px 10px 0;
    background: linear-gradient(200deg, var(--art-dark) 0%, var(--art-dark) 35%, var(--art-mid) 70%, rgba(111,125,88,0) 100%);
    opacity: .85;
  }
  .title {
    position: absolute; left: 0; top: 0; width: 100%;
    font-weight: inherit;
  }
  .title-row {
    position: absolute; left: 0; height: 100px; width: 100%;
  }
  .title-row:nth-child(1) { top: 150px; }
  .title-row:nth-child(2) { top: 262px; }
  .title-row:nth-child(3) { top: 374px; }
  .title-row:nth-child(4) { top: 486px; }
  .title-icon {
    position: absolute; left: 18px; top: 12px; width: 76px; height: 76px;
    display: flex; align-items: center; justify-content: center;
  }
  .title-icon svg { width: 70px; height: 70px; fill: var(--ink); }
  .icon-placeholder {
    width: 64px; height: 72px; border-radius: 40% 40% 50% 50%;
    background: var(--ink);
  }
  .title-word {
    position: absolute; left: 108px; top: 0;
    font-size: 100px; font-weight: 500; line-height: 100px;
    color: var(--title-red); letter-spacing: -1px;
    text-transform: uppercase; white-space: nowrap;
  }
  .subtitle {
    position: absolute; left: 0; width: 100%; top: 612px;
    text-align: center; color: var(--ink);
    font-size: 23px; font-weight: 700; text-transform: uppercase;
  }
  .author {
    position: absolute; left: 0; width: 100%; top: 650px;
    text-align: center; color: var(--ink);
    font-size: 17px; font-weight: 500; letter-spacing: 5px;
    text-transform: uppercase;
  }
</style>
</head>
<body>
<main class="stage">
  <section class="cover">
    <div class="hero-art" role="img" aria-label="Engraved illustration of a set of bagpipes with drones and ribbons"></div>

    <h1 class="title">
      <span class="title-row">
        <span class="title-icon">
          <svg viewBox="0 0 72 72" aria-hidden="true">
            <path d="M10 66 L6 62 L40 28 L44 32 Z"/>
            <ellipse cx="52" cy="18" rx="10" ry="14" transform="rotate(45 52 18)"/>
            <path d="M62 66 L66 62 L32 28 L28 32 Z"/>
            <path d="M8 6 L10 4 L28 22 L26 24 Z M14 2 L16 0 L32 16 L30 18 Z M4 12 L6 10 L22 26 L20 28 Z M20 24 L30 34 L34 30 L24 20 Z"/>
          </svg>
        </span>
        <span class="title-word">Rise</span>
      </span>
      <span class="title-row">
        <span class="title-icon">
          <svg viewBox="0 0 72 72" aria-hidden="true">
            <rect x="2" y="10" width="7" height="56"/>
            <circle cx="20" cy="30" r="8"/>
            <path d="M30 24 H64 A6 6 0 0 1 70 30 V66 H63 V56 H9 V42 H30 Z"/>
          </svg>
        </span>
        <span class="title-word">Hum</span>
      </span>
      <span class="title-row">
        <span class="title-icon">
          <span class="icon-placeholder" role="img" aria-label="Bagpipe silhouette icon"></span>
        </span>
        <span class="title-word">March</span>
      </span>
      <span class="title-row">
        <span class="title-icon">
          <svg viewBox="0 0 72 72" aria-hidden="true">
            <path d="M8 40 V30 A12 12 0 0 1 20 18 H50 V8 L68 24 L50 40 V30 H22 A4 4 0 0 0 18 34 V40 Z"/>
            <path d="M64 32 V42 A12 12 0 0 1 52 54 H22 V64 L4 48 L22 32 V42 H50 A4 4 0 0 0 54 38 V32 Z"/>
          </svg>
        </span>
        <span class="title-word">Rest</span>
      </span>
    </h1>

    <p class="subtitle">Music for the bagpipes</p>
    <p class="author">By Dermot Fairley</p>
  </section>
</main>
</body>
</html>
```